Business Card and Letterhead for new company Corvalt GreenWorks, Inc.

Corvalt GreenWorks, Inc., an engineering and construction firm that provides services for solid waste landfill gas systems, needs a business card and letterhead. We recently had a logo designed but we are open to some tweaks to logo design and color scheme. Generally, we like "earthy" color tones - greens, browns, oranges. This is a sister company - www.taldrickengineering.example.

Target Market(s)

Solid waste landfill companies - Binford Disposal, Keystell Holdings, etc.

Industry/Entity Type

Engineering and Construction

Contact Information for Business Card

Name, Title, email, mobile phone, work phone, website. Potential list of services for back of card: LFG Engineering and Design, GCCS Planning and Operational Consulting, Compliance Monitoring and Reporting, Routine Operations & Maintenance, Nonroutine O&M, Construction Management, Construction QA, GCCS Construction

Font styles to use
Sans Serif

Requirements
Must have
• Logo, pertinent information, maybe a tagline (still in development)
Nice to have
• For back of card, considering an engineering scale (attached for another business of ours), but want to look at other options, alternatives. Like the idea of the back of card to have some utility (scale, unit conversion info, list of services) but willing to consider lots of options.
Should not have
• Needs to have a professional (engineering) and technical look, not cartoonish.

```html
<!DOCTYPE html>
<html lang="en">
<head>
<meta charset="utf-8">
<title>Corvalt GreenWorks – Business Card</title>
<link rel="stylesheet" href="https://fonts.googleapis.com/css2?family=Michroma&family=Open+Sans:wght@400;600;700&display=swap">
<style>
  :root {
    --page-bg: #2a2b2d;
    --card-bg: #1c1d1f;
    --card-back-bg: #111213;
    --brand-green: #7ac143;
    --brand-blue: #2a9fc2;
    --text-light: #f2f2f2;
    --rule-grey: #6b6c6e;
    --gloss-light: #5a5b5e;
    --gloss-mid: #333436;
    --gloss-dark: #0a0a0b;
  }
  html, body {
    margin: 0;
    padding: 0;
    width: 1200px;
    height: 1108px;
    overflow: hidden;
    background: var(--page-bg);
  }
  .canvas {
    position: relative;
    width: 1200px;
    height: 1108px;
  }
  .card {
    position: absolute;
    top: 229px;
    width: 420px;
    height: 650px;
    border-radius: 18px;
    box-shadow: 0 18px 40px rgba(0,0,0,0.55);
    overflow: hidden;
  }
  .card-front {
    left: 150px;
    background: var(--card-bg);
  }
  .card-back {
    left: 630px;
    background: var(--card-back-bg);
  }

  /* Front */
  .brand {
    position: absolute;
    top: 140px;
    left: 0;
    right: 0;
    display: flex;
    align-items: center;
    justify-content: center;
    gap: 14px;
  }
  .brand-mark {
    width: 30px;
    height: 30px;
    border-radius: 50%;
    background: var(--brand-green);
    flex: none;
  }
  .brand-name {
    font-family: "Open Sans", sans-serif;
    font-weight: 700;
    font-size: 33px;
    color: var(--brand-green);
    letter-spacing: 0.2px;
    white-space: nowrap;
  }
  .person {
    position: absolute;
    top: 378px;
    left: 0;
    right: 0;
    text-align: center;
  }
  .person-name {
    font-family: "Michroma", sans-serif;
    font-weight: 400;
    font-size: 24px;
    color: var(--brand-green);
    text-transform: uppercase;
    letter-spacing: 0.5px;
    margin: 0;
  }
  .person-title {
    font-family: "Michroma", sans-serif;
    font-size: 14px;
    color: var(--brand-blue);
    margin: 6px 0 0;
    letter-spacing: 1px;
  }
  .icon-row {
    position: absolute;
    top: 462px;
    left: 40px;
    right: 40px;
    display: flex;
    align-items: center;
    justify-content: center;
    gap: 9px;
  }
  .icon-rule {
    flex: 1;
    height: 1px;
    background: var(--rule-grey);
  }
  .icon-tile {
    width: 32px;
    height: 32px;
    border-radius: 5px;
    background: var(--brand-green);
    display: flex;
    align-items: center;
    justify-content: center;
  }
  .contact-list {
    position: absolute;
    top: 512px;
    left: 0;
    right: 0;
    margin: 0;
    padding: 0;
    list-style: none;
    text-align: center;
    font-family: "Open Sans", sans-serif;
    font-size: 19px;
    line-height: 28px;
    color: var(--text-light);
  }

  /* Back */
  .gloss-pattern {
    position: absolute;
    inset: 0;
    background:
      radial-gradient(ellipse 70% 55% at 95% 20%, rgba(120,121,124,0.55) 0%, rgba(120,121,124,0) 70%),
      radial-gradient(ellipse 60% 45% at 10% 72%, rgba(0,0,0,0.8) 0%, rgba(0,0,0,0) 75%),
      linear-gradient(210deg, var(--gloss-light) 0%, var(--gloss-mid) 38%, #1b1c1d 62%, var(--gloss-dark) 100%);
  }
  .back-brand {
    position: absolute;
    top: 262px;
    right: 28px;
    display: flex;
    align-items: center;
    gap: 9px;
  }
  .back-brand .brand-mark {
    width: 22px;
    height: 22px;
  }
  .back-brand .brand-name {
    font-size: 17px;
  }
  .service-list {
    position: absolute;
    top: 425px;
    left: 0;
    right: 0;
    margin: 0;
    padding: 0;
    list-style: none;
    text-align: center;
    font-family: "Open Sans", sans-serif;
    font-size: 17.5px;
    line-height: 26px;
    color: var(--text-light);
  }
</style>
</head>
<body>
<main class="canvas">

  <section class="card card-front" aria-label="Business card front">
    <div class="brand">
      <span class="brand-mark"></span>
      <span class="brand-name">Corvalt GreenWorks</span>
    </div>

    <div class="person">
      <h1 class="person-name">Marcus Delane</h1>
      <p class="person-title">Managing Director</p>
    </div>

    <div class="icon-row">
      <span class="icon-rule"></span>
      <span class="icon-tile" aria-label="Work phone">
        <svg width="19" height="19" viewBox="0 0 24 24"><path fill="#fff" d="M6.6 10.8a15 15 0 0 0 6.6 6.6l2.2-2.2c.3-.3.7-.4 1-.2 1.1.4 2.3.6 3.6.6.6 0 1 .4 1 1V20c0 .6-.4 1-1 1A17 17 0 0 1 3 4c0-.6.4-1 1-1h3.5c.6 0 1 .4 1 1 0 1.3.2 2.5.6 3.6.1.3 0 .7-.2 1z"/></svg>
      </span>
      <span class="icon-tile" aria-label="Mobile phone">
        <svg width="19" height="19" viewBox="0 0 24 24"><rect x="7" y="2" width="10" height="20" rx="2" fill="none" stroke="#fff" stroke-width="2"/><circle cx="12" cy="18" r="1.2" fill="#fff"/></svg>
      </span>
      <span class="icon-tile" aria-label="Email">
        <svg width="19" height="19" viewBox="0 0 24 24"><rect x="3" y="5" width="18" height="14" rx="1" fill="#fff"/><path d="M3 6l9 7 9-7" fill="none" stroke="#7ac143" stroke-width="1.6"/></svg>
      </span>
      <span class="icon-tile" aria-label="Website">
        <svg width="19" height="19" viewBox="0 0 24 24"><circle cx="12" cy="12" r="9" fill="none" stroke="#fff" stroke-width="2"/><path d="M3 12h18M12 3c3 3 3 15 0 18M12 3c-3 3-3 15 0 18" fill="none" stroke="#fff" stroke-width="1.5"/></svg>
      </span>
      <span class="icon-rule"></span>
    </div>

    <ul class="contact-list">
      <li>055-318 472 906</li>
      <li>055-318 472 906</li>
      <li>info@corvaltmail.example</li>
      <li>www.corvaltgreen.example</li>
    </ul>
  </section>

  <section class="card card-back" aria-label="Business card back">
    <div class="gloss-pattern" role="img" aria-label="Tonal spot-gloss repeating brand mark pattern, lighter grey at top right fading to black at bottom left"></div>
    <div class="back-brand">
      <span class="brand-mark"></span>
      <span class="brand-name">Corvalt GreenWorks</span>
    </div>
    <ul class="service-list">
      <li>LFG Engineering and Design</li>
      <li>GCCS Planning and Operational Consulting</li>
      <li>Compliance Monitoring and Reporting</li>
      <li>Routine Operations &amp; Maintenance</li>
      <li>Nonroutine O&amp;M, Construction Management</li>
      <li>Construction QA, GCCS Construction</li>
    </ul>
  </section>

</main>
</body>
</html>
```